Keltby Swimming Club needs a poster to gain new members

We need a poster design to put up on noticeboards etc. to gain new members.
KELTBY SWIMMING CLUB
Outdoor 50m pool
Gold Level (National) Coach - over 30 years experience
Bronze Licence Assistant Coach
Our squads -
State/National (includes Pool, Surf, Triathletes)
Development Squad
Junior Squad (from 8 years of age)
Every member is valued and every swimmer is provided the opportunity to realise their dreams and potential.
Family atmosphere encouraging a healthy mix of social activities and fun.
State Champion Open Water Swimming Club since 2000.
New members welcome - contact Darren Walsh - keltby.coaching@swimpostmail.net or 0417 860 294
(OUR COLOURS ARE NAVY BLUE, LIGHT BLUE AND WHITE SO WOULD LIKE THE COLOUR SCHEME OF THE POSTER TO SUIT).
A PICTURE OF OUR TSHIRT IS SHOWN ONLY AS I WOULD LIKE THE LETTERING OF KELTBY SWIMMING CLUB TO BE SIMILAR ON THE POSTER.
basically the poster needs to be eye catching to get people to stop and read and want to join our club!!!!

```html
<!DOCTYPE html>
<html lang="en">
<head>
<meta charset="utf-8">
<title>Keltby Swimming Club – Membership Poster</title>
<link rel="stylesheet" href="https://fonts.googleapis.com/css2?family=Bowlby+One&family=Roboto+Condensed:wght@700;800&display=swap">
<style>
  :root {
    --stage: #e9ebed;
    --paper: #f4f9fc;
    --sky-pale: #d7ecf8;
    --sky: #8fcbeb;
    --sky-mid: #5eb1df;
    --ocean: #2f8fcf;
    --navy: #0f5a99;
    --deep: #0b3f73;
    --white: #ffffff;
  }
  * { margin: 0; padding: 0; box-sizing: border-box; }
  html, body { width: 1200px; height: 848px; overflow: hidden; background: var(--stage); }
  .poster {
    position: absolute; left: 290px; top: 24px; width: 620px; height: 800px;
    background: linear-gradient(180deg, var(--paper) 0%, var(--sky-pale) 20%, var(--sky) 55%, var(--sky-mid) 100%);
    overflow: hidden;
    box-shadow: 0 2px 8px rgba(0,0,0,.25);
  }
  .side-pattern {
    position: absolute; top: 125px; width: 120px; height: 405px;
    background: radial-gradient(circle at 50% 40%, var(--sky-pale) 0%, var(--sky) 45%, var(--sky-mid) 100%);
    opacity: .9;
  }
  .side-pattern--left { left: 0; border-radius: 0 60px 60px 0; }
  .side-pattern--right { right: 0; border-radius: 60px 0 0 60px; }
  .masthead { position: absolute; left: 0; right: 0; top: 48px; text-align: center; font-family: "Bowlby One", sans-serif; }
  .masthead__name {
    display: block; font-size: 106px; line-height: 100px; letter-spacing: 2px;
    color: var(--ocean);
    -webkit-text-stroke: 3px var(--navy);
    text-shadow: 0 0 0 var(--white), 4px 4px 0 var(--white), -4px -4px 0 var(--white), 4px -4px 0 var(--white), -4px 4px 0 var(--white), 0 0 10px var(--sky);
  }
  .masthead__sub {
    display: block; margin-top: 14px; font-size: 48px; line-height: 50px;
    color: var(--ocean);
    -webkit-text-stroke: 2px var(--navy);
    text-shadow: 3px 3px 0 var(--white), -3px -3px 0 var(--white), 3px -3px 0 var(--white), -3px 3px 0 var(--white);
  }
  .team-photo-card {
    position: absolute; left: 122px; top: 232px; width: 386px; height: 296px;
    background: var(--sky-pale); transform: rotate(-1.5deg); opacity: .75;
  }
  .team-photo {
    position: absolute; left: 131px; top: 240px; width: 370px; height: 284px;
    border: 6px solid var(--white);
    background: linear-gradient(180deg, #d9c7a6 0%, #b7c9d6 30%, #1d2f55 55%, #22355c 80%, #a58d70 100%);
    box-shadow: 0 2px 6px rgba(0,0,0,.3);
  }
  .info-band {
    position: absolute; left: 0; right: 0; top: 530px; height: 188px;
    background: linear-gradient(180deg, rgba(47,143,207,.55), rgba(47,143,207,.35));
  }
  .info {
    position: absolute; left: 32px; top: 540px; width: 360px;
    font-family: "Roboto Condensed", sans-serif; font-weight: 700; color: var(--white);
    text-shadow: 1px 1px 2px var(--deep);
  }
  .info__head { font-size: 19px; line-height: 23px; font-weight: 800; }
  .info__line { font-size: 15.5px; line-height: 20px; }
  .info__gap { margin-top: 6px; }
  .pool-photo {
    position: absolute; left: 403px; top: 526px; width: 192px; height: 192px; border-radius: 50%;
    border: 5px solid var(--white);
    background: linear-gradient(180deg, #4d8fd6 0%, #9cc8ee 35%, #3c7a3a 48%, #1ea0d6 60%, #54c3ea 75%, #c9a27a 100%);
    box-shadow: 0 2px 6px rgba(0,0,0,.3);
  }
  .footer {
    position: absolute; left: 0; right: 0; top: 722px; text-align: center;
    font-family: "Roboto Condensed", sans-serif; font-weight: 700; font-size: 11.6px; line-height: 14.5px;
    color: var(--white); text-shadow: 1px 1px 1px var(--deep);
  }
</style>
</head>
<body>
  <main class="poster">
    <div class="side-pattern side-pattern--left" role="img" aria-label="Light blue decorative wave and swirl pattern"></div>
    <div class="side-pattern side-pattern--right" role="img" aria-label="Light blue decorative wave and swirl pattern"></div>

    <h1 class="masthead">
      <span class="masthead__name">KELTBY</span>
      <span class="masthead__sub">SWIMMING CLUB</span>
    </h1>

    <div class="team-photo-card"></div>
    <div class="team-photo" role="img" aria-label="Club swimmers in navy team shirts gathered by the pool holding a sponsor banner"></div>

    <div class="info-band"></div>
    <section class="info">
      <p class="info__head">Outdoor 50m pool</p>
      <p class="info__head">Gold Level (National) Coach</p>
      <p class="info__line">- over 30 years experience</p>
      <p class="info__line info__gap">Bronze Licence Assistant Coach</p>
      <p class="info__head info__gap">Our squads -</p>
      <p class="info__line">State/National (includes Pool, Surf, Triathletes)</p>
      <p class="info__line">Development Squad</p>
      <p class="info__line">Junior Squad (from 8 years of age)</p>
    </section>
    <div class="pool-photo" role="img" aria-label="Outdoor 50 metre pool with lane ropes under a blue sky"></div>

    <footer class="footer">
      <p>Every member is valued and every swimmer is provided the opportunity to realise their dreams and potential.</p>
      <p>Family atmosphere encouraging a healthy mix of social activities and fun.</p>
      <p>State Champion Open Water Swimming Club since 2000.</p>
      <p>New members welcome - contact Darren Walsh - keltby.coaching@swimpostmail.net or 0417 860 294</p>
    </footer>
  </main>
</body>
</html>
```